Business card for massage therapy company called Brook Fern Wellness

Need business card for massage therapy company called Brook Fern Wellness. Would like my logo on the front and the back of the card I have 3 options of logos and you can play with what looks better.

Would like this information displayed on the back of the card:

Marcus Ellery
Licensed Massage Therapist
321-555-0147
brookfern-example.com
brookfern_rest_

```html
<!DOCTYPE html>
<html lang="en">
<head>
<meta charset="utf-8">
<title>Brook Fern Wellness – Business Card</title>
<link rel="stylesheet" href="https://fonts.googleapis.com/css2?family=Montserrat:wght@400&family=Tinos&display=swap">
<style>
  :root {
    --backdrop: #2a2a2a;
    --sage: #737a62;
    --sage-ink: #6b705c;
    --tan: #c49c80;
    --paper: #ffffff;
    --body-ink: #5e5e58;
  }
  * { box-sizing: border-box; margin: 0; padding: 0; }
  html, body {
    width: 1200px; height: 1200px; overflow: hidden;
    background: var(--backdrop);
  }
  .sheet {
    position: relative; width: 1200px; height: 1200px;
  }
  .card {
    position: absolute; left: 150px; width: 900px; height: 514px;
    box-shadow: 0 6px 18px rgba(0,0,0,.45);
  }
  .card--front { top: 46px; background: var(--sage); }
  .card--back  { top: 640px; background: var(--paper); }

  .wordmark {
    font-family: "Montserrat", sans-serif;
    font-weight: 400;
    text-transform: uppercase;
    letter-spacing: .28em;
    text-align: center;
    line-height: 1.35;
  }
  .card--front .wordmark {
    position: absolute; inset: 0;
    display: flex; flex-direction: column; justify-content: center; align-items: center;
    color: var(--paper); font-size: 46px;
  }
  .wordmark__small { font-size: .5em; letter-spacing: .6em; }

  .card--back .wordmark {
    position: absolute; left: 40px; top: 0; width: 370px; height: 514px;
    display: flex; flex-direction: column; justify-content: center; align-items: center;
    color: var(--sage-ink); font-size: 30px;
  }
  .divider {
    position: absolute; left: 440px; top: 130px; width: 1.5px; height: 250px;
    background: var(--sage-ink);
  }
  .contact-block {
    position: absolute; left: 490px; top: 150px; width: 380px;
  }
  .person-name {
    font-family: "Montserrat", sans-serif; font-weight: 400;
    font-size: 30px; letter-spacing: .04em; text-transform: uppercase;
    color: var(--sage-ink); word-spacing: .25em;
  }
  .person-title {
    font-family: "Tinos", serif; font-size: 22px; letter-spacing: .04em;
    color: var(--tan); margin-top: 2px;
  }
  .contact-list { list-style: none; margin-top: 30px; }
  .contact-list li {
    display: flex; align-items: center; gap: 14px;
    font-family: "Tinos", serif; font-size: 21px; letter-spacing: .03em;
    color: var(--body-ink); line-height: 30px;
  }
  .contact-icon { width: 20px; height: 20px; flex: none; }
</style>
</head>
<body>
<main class="sheet">
  <section class="card card--front" aria-label="Card front">
    <div class="wordmark">
      <span>Brook Fern</span>
      <span class="wordmark__small">Wellness</span>
    </div>
  </section>

  <section class="card card--back" aria-label="Card back">
    <div class="wordmark">
      <span>Brook Fern</span>
      <span class="wordmark__small">Wellness</span>
    </div>
    <div class="divider"></div>
    <div class="contact-block">
      <p class="person-name">Marcus Ellery</p>
      <p class="person-title">Licensed Massage Therapist</p>
      <ul class="contact-list">
        <li>
          <svg class="contact-icon" viewBox="0 0 20 20" aria-hidden="true">
            <circle cx="10" cy="10" r="10" fill="var(--tan)"/>
            <path d="M7 5.5c.6-.4 1.2-.2 1.5.4l.6 1.3c.2.5 0 .9-.4 1.2l-.5.3c.4 1.3 1.3 2.3 2.5 2.9l.4-.5c.3-.4.8-.5 1.2-.3l1.3.7c.5.3.7.9.3 1.4-.6.9-1.6 1.2-2.6.8C8.6 12.8 6.9 10.6 6.4 8c-.2-1 .1-2 .6-2.5z" fill="#fff"/>
          </svg>
          <span>321-555-0147</span>
        </li>
        <li>
          <svg class="contact-icon" viewBox="0 0 20 20" aria-hidden="true">
            <circle cx="10" cy="10" r="10" fill="var(--tan)"/>
            <rect x="5" y="6.5" width="10" height="7" fill="none" stroke="#fff" stroke-width="1.2"/>
            <path d="M5 6.5l5 4 5-4" fill="none" stroke="#fff" stroke-width="1.2"/>
          </svg>
          <span>brookfern-example.com</span>
        </li>
        <li>
          <svg class="contact-icon" viewBox="0 0 20 20" aria-hidden="true">
            <circle cx="10" cy="10" r="10" fill="var(--tan)"/>
            <g fill="none" stroke="#fff" stroke-width="1">
              <circle cx="10" cy="10" r="5"/>
              <ellipse cx="10" cy="10" rx="2.2" ry="5"/>
              <path d="M5 10h10M6 7.5h8M6 12.5h8"/>
            </g>
          </svg>
          <span>brookfern_rest_</span>
        </li>
      </ul>
    </div>
  </section>
</main>
</body>
</html>
```